Business Card Design

Business Card for professional consulting firm working with large financial institutions.

Target Market(s)

Executive buyers

Industry/Entity Type

Banking

Contact Information for Business Card

Mild creativity wanted. Not boring, but do elaborate artwork.

Font styles to use
Serif
Sans Serif

Colors

Designer to choose colors to be used in the design.

Requirements
Must have
• Standard business card features - company name, individual name, telephone, website, email, locations.
Nice to have
• Two colors
Should not have
• too many colors, fancy printing, cartoons.

```html
<!DOCTYPE html>
<html lang="en">
<head>
<meta charset="utf-8">
<title>Northvale Business Card</title>
<link href="https://fonts.googleapis.com/css2?family=Lora:wght@400&family=Work+Sans:wght@400;500&display=swap" rel="stylesheet">
<style>
  :root {
    --bg: #2b2b2b;
    --charcoal: #48484a;
    --silver: #b9b9bb;
    --paper: #ffffff;
    --ink: #3a3a3c;
    --name-grey: #c4c4c6;
  }
  * { margin: 0; padding: 0; box-sizing: border-box; }
  html, body { width: 1200px; height: 930px; overflow: hidden; }
  body {
    background: var(--bg);
    position: relative;
    font-family: "Work Sans", sans-serif;
  }
  .card {
    position: absolute;
    width: 560px;
    height: 320px;
    border-radius: 16px;
    overflow: hidden;
    left: 320px;
  }
  .card--front { top: 115px; background: var(--charcoal); }
  .card--back { top: 495px; background: var(--paper); }

  .brand {
    font-family: "Lora", serif;
    font-weight: 400;
    display: flex;
    align-items: center;
    gap: 10px;
  }
  .brand__dot {
    width: 12px; height: 12px; border-radius: 50%;
    background: currentColor;
  }
  .card--front .brand {
    position: absolute;
    left: 50%; top: 50%;
    transform: translate(-50%, -50%);
    color: var(--paper);
    font-size: 46px;
  }
  .card__waves { position: absolute; inset: 0; }
  .card--back .brand {
    position: absolute;
    left: 52px; top: 160px;
    color: var(--ink);
    font-size: 28px;
    line-height: 1;
  }
  .card--back .brand__dot { width: 9px; height: 9px; }
  .person {
    position: absolute;
    right: 46px; top: 112px;
    text-align: right;
    width: 250px;
    border-bottom: 1.5px solid var(--ink);
    padding-bottom: 4px;
  }
  .person__name {
    font-family: "Arial", sans-serif;
    font-size: 20px;
    color: var(--name-grey);
    letter-spacing: 0.5px;
    line-height: 1.1;
  }
  .person__title { font-size: 12px; color: var(--ink); }
  .address {
    position: absolute;
    right: 46px; top: 176px;
    text-align: right;
    font-size: 13px;
    line-height: 1.35;
    color: var(--ink);
  }
  .contacts {
    position: absolute;
    left: 40px; top: 232px;
    width: 300px;
    border-top: 1.5px solid var(--ink);
    padding-top: 8px;
    list-style: none;
    font-size: 14px;
    line-height: 1.3;
    color: var(--ink);
  }
  .contacts li { display: flex; align-items: center; gap: 8px; }
  .contacts svg { width: 10px; height: 10px; flex: none; }
</style>
</head>
<body>
  <section class="card card--front">
    <div class="brand"><span class="brand__dot"></span>northvale</div>
  </section>

  <section class="card card--back">
    <svg class="card__waves" viewBox="0 0 560 320" width="560" height="320" aria-hidden="true">
      <path d="M0 0 H560 V58 C450 60 380 92 280 106 C180 118 80 98 0 96 Z" fill="var(--charcoal)"/>
      <path d="M0 96 C80 98 180 118 280 106 C380 92 450 60 560 58 V70 C450 72 380 106 280 120 C180 134 80 122 0 124 Z" fill="var(--silver)"/>
      <path d="M0 124 C80 122 180 134 280 120 C190 144 90 138 0 150 Z" fill="var(--charcoal)"/>
    </svg>
    <div class="brand"><span class="brand__dot"></span>northvale</div>
    <div class="person">
      <div class="person__name">DANIEL HARTLEY</div>
      <div class="person__title">Director</div>
    </div>
    <div class="address">27 Orchard Ln,<br>Riverton VIC 3651</div>
    <ul class="contacts">
      <li><svg viewBox="0 0 10 10"><path d="M2 1 L4 3 L3 4 C4 6 5 7 6 7 L7 6 L9 8 L8 9 C4 9 1 6 1 2 Z" fill="var(--ink)"/></svg>+330 5812-4470</li>
      <li><svg viewBox="0 0 10 10"><rect x="0.5" y="2" width="9" height="6" fill="none" stroke="var(--ink)"/><path d="M0.5 2 L5 5.5 L9.5 2" fill="none" stroke="var(--ink)"/></svg>info@northvale.com</li>
      <li><svg viewBox="0 0 10 10"><circle cx="5" cy="5" r="4.3" fill="none" stroke="var(--ink)"/><path d="M0.7 5 H9.3 M5 0.7 C3 3 3 7 5 9.3 M5 0.7 C7 3 7 7 5 9.3" fill="none" stroke="var(--ink)" stroke-width="0.8"/></svg>www.northvale.com</li>
    </ul>
  </section>
</body>
</html>
```